Willow Bramble Grounds - Lindell Creek Path

Please use this range of Flyers. Info can be found on our Facebook Page Willow Bramble Grounds. W

Colour range- Black with Orange Trim. Logo attached.

Target Market(s)

Horse Owners

Colors
ffcf3e
f78f20
f37122

Requirements
Must have
• Our Logo. Tri-fold
Should not have
• Other photos other than supplied. Do not mix Willow Bramble Grounds with Willow Bramble Equine Sanctuary. This is only for Willow Bramble Grounds.

```html
<!DOCTYPE html>
<html lang="en">
<head>
<meta charset="utf-8">
<title>Willow Bramble Grounds – Tri-fold Brochure</title>
<link href="https://fonts.googleapis.com/css2?family=Tinos:wght@400;700&display=swap" rel="stylesheet">
<style>
  :root {
    --backdrop: #3a3a3c;
    --paper: #f4f4f4;
    --black: #1b1b1c;
    --black-soft: #2c2c2e;
    --orange: #f37122;
    --orange-light: #f78f20;
    --gold: #ffcf3e;
    --peach: #f7a86a;
    --ink: #1e1e1e;
    --white: #ffffff;
  }
  * { box-sizing: border-box; margin: 0; padding: 0; }
  html, body { width: 831px; height: 1200px; overflow: hidden; }
  body {
    background: var(--backdrop);
    font-family: "Tinos", "Times New Roman", serif;
    color: var(--ink);
    position: relative;
  }
  .spread {
    position: absolute;
    left: 55px;
    width: 720px;
    height: 556px;
    background: var(--paper);
    box-shadow: 0 10px 24px rgba(0,0,0,.45);
    overflow: hidden;
  }
  .spread--outside { top: 29px; }
  .spread--inside { top: 615px; }
  .spread svg.art { position: absolute; inset: 0; width: 720px; height: 556px; }
  .fold { position: absolute; top: 0; bottom: 0; width: 240px; }
  .fold--shade { background: linear-gradient(90deg, rgba(0,0,0,.06), rgba(0,0,0,0) 30%); }

  .copy { position: absolute; font-size: 8.4px; line-height: 1.22; }
  .copy p + p { margin-top: 7px; }
  .copy--small { font-size: 7.8px; }
  .copy--light { color: var(--white); }
  .copy--center { text-align: center; }

  .brand {
    position: absolute; top: 26px; right: 34px;
    display: flex; align-items: center; gap: 8px;
  }
  .brand__name {
    color: var(--orange);
    font-size: 19px; line-height: 1.02; text-align: right;
    font-weight: 400; letter-spacing: .5px; text-transform: uppercase;
  }
  .brand__mark { width: 40px; height: 40px; background: var(--orange); }

  .contact {
    position: absolute; left: 260px; top: 330px; width: 200px;
    color: var(--white); text-align: center;
  }
  .contact__title {
    font-size: 13px; font-weight: 700; letter-spacing: .4px;
    padding-bottom: 4px; border-bottom: 1px solid var(--orange);
    margin: 0 14px 6px;
  }
  .contact__line { font-size: 9px; line-height: 1.4; display: flex; justify-content: center; align-items: center; gap: 4px; }
  .contact__line svg { flex: none; }
  .contact__address { font-size: 9px; line-height: 1.25; margin: 2px 0 3px; }
  .social-dot { width: 8px; height: 8px; border-radius: 50%; background: var(--orange); display: inline-block; }

  .phone-pill {
    position: absolute;
    display: flex; align-items: center; gap: 6px;
    background: linear-gradient(90deg, var(--orange), var(--orange-light));
    color: var(--white);
    border: 1.5px solid rgba(255,255,255,.7);
    border-radius: 14px;
    font-weight: 700;
  }
  .phone-pill--cover { left: 530px; top: 470px; padding: 4px 12px 4px 6px; font-size: 14px; }
  .phone-pill__icon {
    width: 18px; height: 18px; border-radius: 50%; background: var(--white);
    display: flex; align-items: center; justify-content: center;
  }

  .call-card {
    position: absolute; left: 515px; top: 440px; width: 185px;
    padding: 8px 10px 9px;
    background: linear-gradient(90deg, var(--orange), var(--orange-light));
    color: var(--white); border-radius: 8px;
    text-align: center; font-weight: 700;
    box-shadow: 0 2px 4px rgba(0,0,0,.2);
  }
  .call-card__lead {
    font-size: 11px; letter-spacing: .5px; text-transform: uppercase; line-height: 1.2;
    padding-bottom: 4px; border-bottom: 1px solid rgba(255,255,255,.8); margin-bottom: 4px;
  }
  .call-card__number { font-size: 17px; display: flex; align-items: center; justify-content: center; gap: 6px; }
</style>
</head>
<body>

<section class="spread spread--outside" aria-label="Brochure outside">
  <svg class="art" viewBox="0 0 720 556">
    <defs>
      <linearGradient id="darkBand" x1="0" y1="0" x2="1" y2="1">
        <stop offset="0" stop-color="#2c2c2e"/>
        <stop offset="1" stop-color="#151516"/>
      </linearGradient>
      <linearGradient id="photoGreen" x1="0" y1="0" x2="0" y2="1">
        <stop offset="0" stop-color="#6f6a5e"/>
        <stop offset=".55" stop-color="#8a7a63"/>
        <stop offset="1" stop-color="#6f8a45"/>
      </linearGradient>
      <linearGradient id="photoBarn" x1="0" y1="0" x2="0" y2="1">
        <stop offset="0" stop-color="#8c8e77"/>
        <stop offset=".5" stop-color="#9b3a30"/>
        <stop offset="1" stop-color="#5f7c3a"/>
      </linearGradient>
    </defs>
    <path d="M0,372 C70,330 150,290 240,282 L300,270 L300,300 C260,300 200,320 150,360 C100,400 40,400 0,400 Z" fill="var(--orange)"/>
    <path d="M0,400 C80,390 150,340 240,305 L480,300 C560,300 640,320 720,292 L720,556 L0,556 Z" fill="url(#darkBand)"/>
    <circle cx="255" cy="262" r="14" fill="var(--peach)" opacity=".8"/>
    <circle cx="430" cy="285" r="22" fill="var(--peach)" opacity=".6"/>
    <circle cx="660" cy="275" r="22" fill="var(--peach)" opacity=".7"/>
    <circle cx="620" cy="300" r="12" fill="var(--orange)" opacity=".6"/>

    <circle cx="130" cy="415" r="112" fill="url(#photoGreen)" stroke="var(--white)" stroke-width="4" role="img" aria-label="Photo: chestnut horse beside a covered wagon with the grounds' name on its canvas"/>
    <circle cx="102" cy="275" r="60" fill="url(#photoGreen)" stroke="var(--white)" stroke-width="4" role="img" aria-label="Photo: handler leading a pony over a low wooden obstacle"/>
    <circle cx="360" cy="215" r="80" fill="url(#photoGreen)" stroke="var(--white)" stroke-width="4" role="img" aria-label="Photo: rider on a roan horse crossing a wooden bridge"/>
    <circle cx="565" cy="222" r="118" fill="url(#photoBarn)" stroke="var(--white)" stroke-width="4" role="img" aria-label="Photo: handler with a grey horse in front of a red timber shelter"/>
    <circle cx="635" cy="265" r="18" fill="var(--white)" opacity=".35"/>
  </svg>
  <div class="fold fold--shade" style="left:240px"></div>
  <div class="fold fold--shade" style="left:480px"></div>

  <div class="copy" style="left:28px; top:40px; width:190px;">
    <p>Lorem ipsum dolor sit amet, consectetur adipiscing elit, sed do eiusmod tempor incididunt ut labore et dolore magna aliqua. Ut enim ad minim veniam, quis nostrud exercitation ullamco laboris nisi ut aliquip ex ea commodo consequat. Duis aute irure dolor in reprehenderit in voluptate velit esse cillum dolore eu fugiat nulla pariatur. Excepteur sint occaecat cupidatat non proident, sunt in culpa qui officia deserunt mollit anim id est laborum.
    Sed ut perspiciatis unde omnis iste natus error sit voluptatem accusantium doloremque laudantium, totam rem aperiam.</p>
  </div>

  <div class="copy copy--center" style="left:262px; top:40px; width:196px;">
    <p>Our amazing property Willow Bramble Grounds is a multi-faceted equine destination for horse owners. Our years of hands-on horse care have honed an experienced team of riders, handlers and carers.</p>
  </div>

  <div class="contact">
    <div class="contact__title">Contact Info</div>
    <div class="contact__line">
      <svg width="8" height="10" viewBox="0 0 8 10"><path d="M4 0a3 3 0 0 1 3 3c0 2-3 6-3 6S1 5 1 3a3 3 0 0 1 3-3z" fill="none" stroke="#fff" stroke-width="1"/><circle cx="4" cy="3" r="1" fill="#fff"/></svg>
    </div>
    <div class="contact__address">48 Fernhill Road Ashby,<br>VIC, Australia 3391</div>
    <div class="contact__line">
      <svg width="9" height="9" viewBox="0 0 10 10"><circle cx="5" cy="5" r="4.4" fill="none" stroke="#fff" stroke-width=".9"/><path d="M3.3 2.8c.4-.3.8 0 1 .5l.2.5-.5.4c.2.6.6 1 1.1 1.2l.4-.5.6.2c.5.2.6.6.3 1-.5.5-1.6.4-2.5-.5s-1.1-2.3-.6-2.8z" fill="#fff"/></svg>
      <span>+61 400 555 019</span>
    </div>
    <div class="contact__line">
      <svg width="9" height="9" viewBox="0 0 10 10"><circle cx="5" cy="5" r="4.4" fill="none" stroke="#fff" stroke-width=".9"/><rect x="2.6" y="3.4" width="4.8" height="3.2" fill="none" stroke="#fff" stroke-width=".7"/><path d="M2.6 3.4 5 5.2 7.4 3.4" fill="none" stroke="#fff" stroke-width=".7"/></svg>
      <span>info@willowbramblevet.com</span>
    </div>
    <div class="contact__line">
      <span class="social-dot"></span>
      <span>/WillowBrambleGrounds</span>
    </div>
  </div>

  <div class="brand">
    <div class="brand__name">Willow<br>Bramble<br>Grounds</div>
    <div class="brand__mark"></div>
  </div>

  <div class="phone-pill phone-pill--cover">
    <span class="phone-pill__icon">
      <svg width="10" height="10" viewBox="0 0 10 10"><path d="M2 1.2c.6-.4 1.2 0 1.5.7l.3.8-.8.6c.3.9.9 1.5 1.7 1.8l.6-.8.9.3c.7.3.9.9.4 1.5-.8.8-2.4.6-3.8-.8S1.2 2 2 1.2z" fill="var(--orange)"/></svg>
    </span>
    <span>+61 400 555 019</span>
  </div>
</section>

<section class="spread spread--inside" aria-label="Brochure inside">
  <svg class="art" viewBox="0 0 720 556">
    <defs>
      <linearGradient id="darkTop" x1="0" y1="0" x2="1" y2="1">
        <stop offset="0" stop-color="#2c2c2e"/>
        <stop offset="1" stop-color="#151516"/>
      </linearGradient>
      <linearGradient id="photoField" x1="0" y1="0" x2="0" y2="1">
        <stop offset="0" stop-color="#7f9a5a"/>
        <stop offset=".6" stop-color="#5c5e62"/>
        <stop offset="1" stop-color="#6f8a45"/>
      </linearGradient>
      <linearGradient id="photoShed" x1="0" y1="0" x2="0" y2="1">
        <stop offset="0" stop-color="#a3352c"/>
        <stop offset=".6" stop-color="#7a6a55"/>
        <stop offset="1" stop-color="#a8794c"/>
      </linearGradient>
    </defs>
    <path d="M0,0 L720,0 L720,305 C660,290 600,300 540,318 C470,338 400,325 330,318 C250,312 170,330 100,322 C60,318 30,312 0,318 Z" fill="url(#darkTop)"/>
    <path d="M0,318 C30,312 60,318 100,322 C170,330 250,312 330,318 L330,336 C250,330 170,345 100,340 C60,337 30,332 0,336 Z" fill="var(--orange)"/>
    <path d="M420,330 C470,338 520,320 540,318 L540,334 C500,342 460,346 420,342 Z" fill="var(--orange)"/>

    <circle cx="132" cy="200" r="112" fill="url(#photoField)" stroke="var(--white)" stroke-width="4" role="img" aria-label="Photo: rider on a grey horse stepping over a rope rail"/>
    <circle cx="330" cy="148" r="74" fill="url(#photoShed)" stroke="var(--white)" stroke-width="4" role="img" aria-label="Photo: shaggy pony on a wooden bridge beside a red shed"/>
    <circle cx="325" cy="290" r="62" fill="url(#photoField)" stroke="var(--white)" stroke-width="4" role="img" aria-label="Photo: handler guiding a palomino pony over timber rails"/>
    <circle cx="600" cy="318" r="86" fill="url(#photoField)" stroke="var(--white)" stroke-width="4" role="img" aria-label="Photo: grey horse walking through hanging coloured ribbons"/>

    <circle cx="80" cy="318" r="30" fill="var(--peach)" opacity=".75"/>
    <circle cx="118" cy="345" r="18" fill="var(--peach)" opacity=".7"/>
    <circle cx="405" cy="240" r="16" fill="var(--peach)" opacity=".7"/>
    <circle cx="555" cy="390" r="26" fill="var(--peach)" opacity=".8"/>
    <circle cx="585" cy="382" r="14" fill="var(--orange)" opacity=".5"/>
  </svg>
  <div class="fold fold--shade" style="left:240px"></div>
  <div class="fold fold--shade" style="left:480px"></div>

  <div class="copy copy--small copy--light" style="left:500px; top:30px; width:200px;">
    <p>Lorem ipsum dolor sit amet, consectetur adipiscing elit, sed do eiusmod tempor incididunt ut labore et dolore magna aliqua. Ut enim ad minim veniam, quis nostrud exercitation ullamco laboris nisi ut aliquip ex ea commodo consequat. Duis aute irure dolor in reprehenderit in voluptate velit esse cillum dolore eu fugiat nulla pariatur. Excepteur sint occaecat cupidatat non proident, sunt in culpa qui officia deserunt mollit anim id est laborum. Sed ut perspiciatis unde omnis iste natus error sit voluptatem accusantium doloremque laudantium, totam rem aperiam.</p>
  </div>

  <div class="copy" style="left:26px; top:372px; width:196px;">
    <p>Lorem ipsum dolor sit amet, consectetur adipiscing elit, sed do eiusmod tempor incididunt ut labore et dolore magna aliqua. Ut enim ad minim veniam, quis nostrud exercitation ullamco laboris nisi ut aliquip ex ea commodo consequat. Duis aute irure dolor in reprehenderit in voluptate velit esse cillum dolore eu fugiat nulla pariatur. Excepteur sint occaecat cupidatat non proident, sunt in culpa qui officia deserunt mollit anim id est laborum. Sed ut perspiciatis unde omnis iste natus error sit voluptatem accusantium doloremque laudantium, totam rem aperiam.</p>
    <p>Nemo enim ipsam voluptatem quia voluptas sit aspernatur aut odit aut fugit, sed quia consequuntur magni dolores eos qui ratione voluptatem sequi nesciunt.</p>
  </div>

  <div class="copy" style="left:262px; top:372px; width:196px;">
    <p>Lorem ipsum dolor sit amet, consectetur adipiscing elit, sed do eiusmod tempor incididunt ut labore et dolore magna aliqua. Ut enim ad minim veniam, quis nostrud exercitation ullamco laboris nisi ut aliquip ex ea commodo consequat. Duis aute irure dolor in reprehenderit in voluptate velit esse cillum dolore eu fugiat nulla pariatur. Excepteur sint occaecat cupidatat non proident, sunt in culpa qui officia deserunt mollit anim id est laborum. Sed ut perspiciatis unde omnis iste natus error sit voluptatem accusantium doloremque laudantium, totam rem aperiam.</p>
    <p>Nemo enim ipsam voluptatem quia voluptas sit aspernatur aut odit aut fugit, sed quia consequuntur magni dolores eos qui ratione voluptatem sequi nesciunt.</p>
  </div>

  <div class="call-card">
    <div class="call-card__lead">For more<br>information call</div>
    <div class="call-card__number">
      <span class="phone-pill__icon">
        <svg width="10" height="10" viewBox="0 0 10 10"><path d="M2 1.2c.6-.4 1.2 0 1.5.7l.3.8-.8.6c.3.9.9 1.5 1.7 1.8l.6-.8.9.3c.7.3.9.9.4 1.5-.8.8-2.4.6-3.8-.8S1.2 2 2 1.2z" fill="var(--orange)"/></svg>
      </span>
      <span>+61 400 555 019</span>
    </div>
  </div>
</section>

</body>
</html>
```